Website design for labour force (commercial truck driver) company

Looking for a Wordpress template (or design files in conjunction with a free Wordpress template).
Company tag line:
Tenvora – On Demand, Professional Drivers
Real Drivers | Real Standards | Real Results
Logo design has already been completed and is attached

Company provides contract drivers to trucking companies. Target market is both the trucking companies looking for drivers and drivers looking for work.
Design to encompass header / footer and basic page design, navigation menu, home page, contact page. Customer will add content and additional pages over time.

```html
<!DOCTYPE html>
<html lang="en">
<head>
<meta charset="utf-8">
<title>Tenvora – On Demand, Professional Drivers</title>
<link href="https://fonts.googleapis.com/css2?family=Arimo:wght@400;500;600;700&display=swap" rel="stylesheet">
<style>
:root{
  --green:#0e7a5b;
  --green-light:#1f9a6f;
  --ink:#1f2937;
  --muted:#4b5563;
  --soft:#f6f8fa;
  --line:#e5e7eb;
  --footer:#2d3748;
  --white:#ffffff;
}
*{box-sizing:border-box;margin:0;padding:0}
html,body{width:1200px;height:3796px;overflow:hidden}
body{font-family:'Arimo',Arial,sans-serif;color:var(--ink);background:var(--white)}
.wrap{width:1040px;margin:0 auto;position:relative}
svg{display:block}

/* header */
.site-header{height:122px;border-bottom:1px solid var(--line)}
.site-header .wrap{display:flex;align-items:center;height:100%;padding-top:30px}
.brand{display:flex;align-items:center;gap:8px;font-weight:700;font-size:16px;color:var(--ink);width:290px}
.brand-dot{width:26px;height:26px;border-radius:50%;background:var(--ink)}
.nav{display:flex;gap:28px;font-size:13px;color:#374151;flex:1}
.header-cta{display:flex;gap:10px}
.btn{display:inline-flex;align-items:center;justify-content:center;gap:8px;font-size:12px;font-weight:600;border-radius:4px;padding:0 14px;height:33px}
.btn-outline{border:1.5px solid var(--green);color:var(--green)}
.btn-solid{background:var(--green);color:var(--white)}

/* hero */
.hero{height:512px;position:relative;text-align:center;color:var(--white);
  background:radial-gradient(ellipse at 80% 40%,#6b6a3a 0%,transparent 45%),radial-gradient(ellipse at 20% 30%,#1f6d85 0%,transparent 50%),linear-gradient(180deg,#0b1a24 0%,#16323d 55%,#2a3035 100%)}
.hero h1{font-size:49px;font-weight:700;line-height:52px;padding-top:104px}
.hero h1 span{color:var(--green-light);display:block}
.hero .tag{font-size:19px;margin-top:26px}
.hero .lead{font-size:14px;line-height:24px;margin-top:28px;opacity:.95}
.hero-actions{display:flex;justify-content:center;gap:12px;margin-top:30px}
.hero-actions .btn{height:36px;font-size:14px;padding:0 26px}
.btn-white{background:var(--white);color:var(--green)}

/* why */
.why{height:471px;background:var(--soft);text-align:center}
.section-title{font-size:29px;font-weight:600;color:var(--ink)}
.section-sub{font-size:14px;line-height:24px;color:var(--muted);margin-top:16px}
.why .section-title{padding-top:68px}
.feature-grid{display:flex;gap:27px;margin-top:56px}
.feature{flex:1;background:var(--white);border-radius:6px;box-shadow:0 1px 3px rgba(0,0,0,.06);height:186px;padding-top:34px}
.feature svg{margin:0 auto}
.feature h3{font-size:16px;font-weight:600;margin-top:20px}
.feature p{font-size:12.5px;line-height:20px;color:var(--muted);margin:12px 24px 0}

/* split sections */
.split{height:509px}
.split .wrap{display:flex;align-items:center;height:100%;gap:40px}
.split.alt{background:var(--soft)}
.split-text{flex:1}
.split-text h2{font-size:30px;font-weight:600}
.split-text .intro{font-size:14px;line-height:24px;color:var(--muted);margin-top:20px;max-width:470px}
.points{list-style:none;margin-top:22px}
.points li{display:flex;gap:10px;margin-bottom:19px}
.points b{display:block;font-size:13px;font-weight:600;color:var(--ink)}
.points span{display:block;font-size:12.5px;color:var(--muted);margin-top:4px}
.split-text .btn{height:33px;margin-top:8px}
.split-media{width:497px;height:372px;border-radius:6px;box-shadow:0 6px 14px rgba(0,0,0,.18)}
.media-fleet{background:linear-gradient(110deg,#2a2c2e 0%,#8a8d90 40%,#d7d9da 70%,#5a5d60 100%)}
.media-lot{background:linear-gradient(135deg,#7b7f83 0%,#a3a6a8 40%,#5c7c86 70%,#8b8e90 100%)}

/* testimonials */
.testimonials{height:467px;text-align:center}
.testimonials .section-title{padding-top:68px}
.quote-grid{display:flex;gap:27px;margin-top:56px;text-align:left}
.quote{flex:1;background:var(--soft);border-radius:6px;height:200px;padding:20px}
.stars{color:var(--green);font-size:15px;letter-spacing:2px}
.quote p{font-size:12.5px;line-height:20px;color:var(--muted);margin-top:10px;min-height:80px}
.person{display:flex;align-items:center;gap:12px;margin-top:10px}
.avatar{width:32px;height:32px;border-radius:50%;background:var(--green);display:flex;align-items:center;justify-content:center}
.person b{display:block;font-size:13px;font-weight:600}
.person span{font-size:11px;color:var(--muted)}

/* contact */
.contact{height:889px;background:var(--soft);text-align:center}
.contact .section-title{padding-top:66px}
.contact-grid{display:flex;gap:40px;margin-top:56px;text-align:left}
.form-card{width:497px;background:var(--white);border-radius:6px;padding:26px 27px;height:623px}
.field{margin-bottom:18px}
.field label{display:block;font-size:11.5px;color:var(--ink);margin-bottom:10px}
.input{border:1px solid var(--line);border-radius:4px;height:34px;font-size:11.5px;color:#6b7280;padding:0 10px;display:flex;align-items:center;justify-content:space-between}
.row{display:flex;gap:14px}
.row .field{flex:1}
.textarea{height:84px;align-items:flex-start;padding-top:10px}
.submit{background:var(--green);color:var(--white);border-radius:4px;height:33px;font-size:12px;font-weight:600;display:flex;align-items:center;justify-content:center;margin-top:20px}
.info-col{flex:1}
.info-card{background:var(--white);border-radius:6px;padding:28px 27px}
.info-card h3{font-size:16px;font-weight:600}
.info-item{display:flex;gap:14px;margin-top:24px;font-size:13px;line-height:20px;color:var(--muted)}
.info-item b{display:block;font-weight:400;color:#374151}
.hours{margin-top:30px;padding-bottom:24px}
.hours h3{display:flex;align-items:center;gap:8px}
.hours-row{display:flex;justify-content:space-between;font-size:12.5px;color:var(--muted);margin-top:16px}
.hours-row:first-of-type{margin-top:24px}

/* footer */
.site-footer{height:318px;background:var(--footer);color:#a0aec0}
.site-footer .wrap{padding-top:46px}
.footer-top{display:flex}
.footer-brand{width:532px}
.footer-brand .brand{color:var(--white);font-size:19px}
.footer-brand .brand-dot{background:var(--white)}
.footer-brand p{font-size:12.5px;line-height:20px;margin-top:22px;max-width:350px}
.social{display:flex;gap:14px;margin-top:14px}
.social i{width:14px;height:14px;border-radius:3px;background:#a0aec0;display:block}
.footer-col{width:266px}
.footer-col h4{color:var(--white);font-size:14px;font-weight:600;margin-bottom:18px}
.footer-col a{display:block;font-size:12.5px;margin-bottom:12px;color:#a0aec0;text-decoration:none}
.footer-bottom{border-top:1px solid #4a5568;margin-top:44px;padding-top:30px;text-align:center;font-size:12px}
</style>
</head>
<body>

<header class="site-header">
  <div class="wrap">
    <div class="brand"><span class="brand-dot"></span>Tenvora</div>
    <nav class="nav"><span>Home</span><span>Services</span><span>For Companies</span><span>For Drivers</span><span>Contact</span></nav>
    <div class="header-cta"><span class="btn btn-outline">Find Drivers</span><span class="btn btn-solid">Find Work</span></div>
  </div>
</header>

<section class="hero" role="img" aria-label="Photo of a truck driving through a lit highway tunnel">
  <h1>Professional Drivers<span>On Demand</span></h1>
  <p class="tag">Real Drivers | Real Standards | Real Results</p>
  <p class="lead">Connecting experienced, professional drivers with trucking companies nationwide.<br>Your trusted partner for reliable transportation solutions.</p>
  <div class="hero-actions">
    <span class="btn btn-white"><svg width="14" height="14" viewBox="0 0 24 24" fill="none" stroke="currentColor" stroke-width="2"><rect x="4" y="3" width="16" height="18" rx="1"/><path d="M9 8h6M9 12h6M9 16h6"/></svg>For Trucking Companies</span>
    <span class="btn btn-solid"><svg width="14" height="14" viewBox="0 0 24 24" fill="none" stroke="currentColor" stroke-width="2"><circle cx="12" cy="8" r="4"/><path d="M4 21c0-4 4-6 8-6s8 2 8 6"/></svg>For Professional Drivers</span>
  </div>
</section>

<section class="why">
  <div class="wrap">
    <h2 class="section-title">Why Choose Tenvora?</h2>
    <p class="section-sub">We bridge the gap between skilled drivers and trucking companies with our<br>comprehensive on-demand driver services.</p>
    <div class="feature-grid">
      <div class="feature">
        <svg width="26" height="26" viewBox="0 0 24 24" fill="none" stroke="#0e7a5b" stroke-width="2"><path d="M3 12V4h8l10 10-8 8z"/><circle cx="7.5" cy="8.5" r="1"/></svg>
        <h3>Certified Professionals</h3>
        <p>All drivers are thoroughly vetted, certified, and maintain the highest safety standards.</p>
      </div>
      <div class="feature">
        <svg width="26" height="26" viewBox="0 0 24 24" fill="none" stroke="#0e7a5b" stroke-width="2"><circle cx="12" cy="12" r="9"/><path d="M12 7v5l3 2"/></svg>
        <h3>On-Demand Availability</h3>
        <p>Quick response times with drivers available when and where you need them most.</p>
      </div>
      <div class="feature">
        <svg width="26" height="26" viewBox="0 0 24 24" fill="none" stroke="#0e7a5b" stroke-width="2"><path d="M12 3l8 3v6c0 5-4 8-8 9-4-1-8-4-8-9V6z"/></svg>
        <h3>Fully Insured</h3>
        <p>Complete insurance coverage and liability protection for peace of mind.</p>
      </div>
    </div>
  </div>
</section>

<section class="split">
  <div class="wrap">
    <div class="split-text">
      <h2>For Trucking Companies</h2>
      <p class="intro">Access a network of professional drivers to meet your transportation needs. Our on-demand service ensures you never miss a delivery deadline.</p>
      <ul class="points">
        <li><svg width="16" height="16" viewBox="0 0 24 24" fill="none" stroke="#0e7a5b" stroke-width="2"><circle cx="12" cy="12" r="9"/><path d="M8 12l3 3 5-6"/></svg><div><b>Qualified Driver Network</b><span>Access to pre-screened, experienced drivers with clean records</span></div></li>
        <li><svg width="16" height="16" viewBox="0 0 24 24" fill="none" stroke="#0e7a5b" stroke-width="2"><circle cx="12" cy="12" r="9"/><path d="M8 12l3 3 5-6"/></svg><div><b>Flexible Scheduling</b><span>Book drivers for short-term or long-term assignments</span></div></li>
        <li><svg width="16" height="16" viewBox="0 0 24 24" fill="none" stroke="#0e7a5b" stroke-width="2"><circle cx="12" cy="12" r="9"/><path d="M8 12l3 3 5-6"/></svg><div><b>Cost-Effective Solutions</b><span>Reduce overhead costs with our efficient driver placement</span></div></li>
      </ul>
      <span class="btn btn-solid">Find Drivers Now <svg width="12" height="12" viewBox="0 0 24 24" fill="none" stroke="currentColor" stroke-width="2.5"><path d="M4 12h16M14 6l6 6-6 6"/></svg></span>
    </div>
    <div class="split-media media-fleet" role="img" aria-label="Photo of a row of parked white semi truck cabs"></div>
  </div>
</section>

<section class="split alt">
  <div class="wrap">
    <div class="split-media media-lot" role="img" aria-label="Aerial photo of trucks parked in a large lot"></div>
    <div class="split-text">
      <h2>For Professional Drivers</h2>
      <p class="intro">Join our network of professional drivers and access consistent, well-paying opportunities with reputable trucking companies.</p>
      <ul class="points">
        <li><svg width="16" height="16" viewBox="0 0 24 24" fill="none" stroke="#0e7a5b" stroke-width="2"><circle cx="12" cy="12" r="9"/><path d="M8 12l3 3 5-6"/></svg><div><b>Competitive Pay Rates</b><span>Earn top dollar with our premium client network</span></div></li>
        <li><svg width="16" height="16" viewBox="0 0 24 24" fill="none" stroke="#0e7a5b" stroke-width="2"><circle cx="12" cy="12" r="9"/><path d="M8 12l3 3 5-6"/></svg><div><b>Flexible Work Schedule</b><span>Choose assignments that fit your lifestyle and preferences</span></div></li>
        <li><svg width="16" height="16" viewBox="0 0 24 24" fill="none" stroke="#0e7a5b" stroke-width="2"><circle cx="12" cy="12" r="9"/><path d="M8 12l3 3 5-6"/></svg><div><b>Professional Support</b><span>Dedicated support team to help you succeed</span></div></li>
      </ul>
      <span class="btn btn-solid">Apply Now <svg width="12" height="12" viewBox="0 0 24 24" fill="none" stroke="currentColor" stroke-width="2.5"><path d="M4 12h16M14 6l6 6-6 6"/></svg></span>
    </div>
  </div>
</section>

<section class="testimonials">
  <div class="wrap">
    <h2 class="section-title">What Our Clients Say</h2>
    <p class="section-sub">Real feedback from trucking companies and drivers who trust Tenvora</p>
    <div class="quote-grid">
      <div class="quote">
        <div class="stars">★★★★★</div>
        <p>"Tenvora saved us during peak season. Their drivers are professional and reliable. We've been using their services for over a year now."</p>
        <div class="person"><span class="avatar"><svg width="14" height="14" viewBox="0 0 24 24" fill="none" stroke="#fff" stroke-width="2"><circle cx="12" cy="8" r="4"/><path d="M4 21c0-4 4-6 8-6s8 2 8 6"/></svg></span><div><b>Dale Corvin</b><span>Fleet Manager, Pinecrest Haulage</span></div></div>
      </div>
      <div class="quote">
        <div class="stars">★★★★★</div>
        <p>"Great pay, flexible schedule, and professional support. Tenvora has helped me maintain steady income while having control over my schedule."</p>
        <div class="person"><span class="avatar"><svg width="14" height="14" viewBox="0 0 24 24" fill="none" stroke="#fff" stroke-width="2"><circle cx="12" cy="8" r="4"/><path d="M4 21c0-4 4-6 8-6s8 2 8 6"/></svg></span><div><b>Nora Ellsby</b><span>Professional Driver</span></div></div>
      </div>
      <div class="quote">
        <div class="stars">★★★★★</div>
        <p>"The quality of drivers from Tenvora is exceptional. They understand the transportation industry and deliver real results for our operations."</p>
        <div class="person"><span class="avatar"><svg width="14" height="14" viewBox="0 0 24 24" fill="none" stroke="#fff" stroke-width="2"><circle cx="12" cy="8" r="4"/><path d="M4 21c0-4 4-6 8-6s8 2 8 6"/></svg></span><div><b>Victor Hale</b><span>Operations Director, Ridgeway Freight</span></div></div>
      </div>
    </div>
  </div>
</section>

<section class="contact">
  <div class="wrap">
    <h2 class="section-title">Get Started Today</h2>
    <p class="section-sub">Ready to connect with professional drivers or find your next opportunity? Contact us now.</p>
    <div class="contact-grid">
      <div class="form-card">
        <div class="field"><label>I am a:</label><div class="input">Select your role<svg width="10" height="10" viewBox="0 0 24 24" fill="none" stroke="#9ca3af" stroke-width="2"><path d="M6 9l6 6 6-6"/></svg></div></div>
        <div class="row">
          <div class="field"><label>First Name</label><div class="input">John</div></div>
          <div class="field"><label>Last Name</label><div class="input">Doe</div></div>
        </div>
        <div class="field"><label>Email</label><div class="input">name@example.com</div></div>
        <div class="field"><label>Phone</label><div class="input">(555) 284-9106</div></div>
        <div class="field"><label>Company/Organization (if applicable)</label><div class="input">Pinecrest Haulage</div></div>
        <div class="field"><label>Message</label><div class="input textarea">Tell us about your needs...</div></div>
        <div class="submit">Send Message</div>
      </div>
      <div class="info-col">
        <div class="info-card">
          <h3>Contact Information</h3>
          <div class="info-item"><svg width="18" height="18" viewBox="0 0 24 24" fill="none" stroke="#0e7a5b" stroke-width="2"><path d="M5 3h4l2 5-3 2a11 11 0 006 6l2-3 5 2v4a2 2 0 01-2 2A18 18 0 013 5a2 2 0 012-2z"/></svg><div><b>Phone</b>(555) 284-9106</div></div>
          <div class="info-item"><svg width="18" height="18" viewBox="0 0 24 24" fill="none" stroke="#0e7a5b" stroke-width="2"><rect x="3" y="5" width="18" height="14" rx="2"/><path d="M3 7l9 6 9-6"/></svg><div><b>Email</b>info@tenvora.com</div></div>
          <div class="info-item"><svg width="18" height="18" viewBox="0 0 24 24" fill="none" stroke="#0e7a5b" stroke-width="2"><path d="M12 22s7-7 7-12a7 7 0 00-14 0c0 5 7 12 7 12z"/><circle cx="12" cy="10" r="2.5"/></svg><div><b>Address</b>48 Harbor Lane<br>Millbrook, State 40721</div></div>
        </div>
        <div class="info-card hours">
          <h3><svg width="16" height="16" viewBox="0 0 24 24" fill="none" stroke="#1f2937" stroke-width="2"><circle cx="12" cy="12" r="9"/><path d="M12 7v5l3 2"/></svg>Business Hours</h3>
          <div class="hours-row"><span>Monday - Friday</span><span>8:00 AM - 6:00 PM</span></div>
          <div class="hours-row"><span>Saturday</span><span>9:00 AM - 3:00 PM</span></div>
          <div class="hours-row"><span>Sunday</span><span>Closed</span></div>
        </div>
      </div>
    </div>
  </div>
</section>

<footer class="site-footer">
  <div class="wrap">
    <div class="footer-top">
      <div class="footer-brand">
        <div class="brand"><span class="brand-dot"></span>Tenvora</div>
        <p>Real Drivers | Real Standards | Real Results<br>Connecting professional drivers with trucking companies nationwide.</p>
        <div class="social"><i></i><i></i><i></i></div>
      </div>
      <div class="footer-col"><h4>Services</h4><a>Driver Placement</a><a>On-Demand Drivers</a><a>Fleet Support</a><a>Driver Training</a></div>
      <div class="footer-col"><h4>Company</h4><a>About Us</a><a>Careers</a><a>Contact</a><a>Privacy Policy</a></div>
    </div>
    <div class="footer-bottom">© 2024 Tenvora. All rights reserved.</div>
  </div>
</footer>

</body>
</html>
```